Tollo is the place for Used Car Inspections

Tollo ONLY sells Used Car Inspections.

We need a website that tells that story simply.

Please be original and don't just copy my mockup. I'm not a designer.

Reason: Too few designers(<10)...too many weak designs(>80). I have subsequently revised my brief, uploaded more defined mockup and have tried to inspire some originality. I have also invited add designs, some who have declined. Any suggestions. Any suggestions?

Reason: Still waiting on original designs

Target Market(s)

Car Buyers

Industry/Entity Type

Used Car

Logo Text

Tollo

Number of Pages Required

5+ page

Font styles to use
Sans Serif

Colors
33a6d7
ffc214

Requirements
Must have
• Why Tollo?
• -Top 5 Questions
• Tollo Certified
• -Graphic detailing inspection
• How it Works
• -Graphic-- 1. Find a Location 2. Personal/Vehicle Info Form 3. Purchase
• -Get a Tollo Inspection
• Get a Tollo Inspection
• -Find a Location
• -Personal/Vehicle info Form
• -Purchase
• Become a Tollo Dealer
• -Form
• -Upload Credentials
• About Us
• Contact Us
• Term & Conditions
• Privacy
• FAQ
• Press
• Social Media
Nice to have
• Customer feedback-Quorra
Should not have
• Not sure

```html
<!DOCTYPE html>
<html lang="en">
<head>
<meta charset="utf-8">
<title>Tollo – Used Car Inspections</title>
<link href="https://fonts.googleapis.com/css2?family=Open+Sans:wght@400;600;700;800&family=Roboto+Condensed:wght@400;700&display=swap" rel="stylesheet">
<style>
:root{
  --blue:#33a6d7;
  --blue-deep:#1d7fb0;
  --yellow:#ffc214;
  --ink:#2b2f33;
  --muted:#6d747a;
  --dark:#1b252d;
  --footer:#212c35;
  --footer-bar:#161e25;
  --white:#ffffff;
  --line:#d9dde0;
}
*{box-sizing:border-box;margin:0;padding:0}
html,body{width:784px;height:1200px;overflow:hidden}
body{font-family:"Open Sans",Arial,sans-serif;color:var(--ink);background:var(--white);position:relative}
.cond{font-family:"Roboto Condensed","Arial Narrow",sans-serif}

/* Hero */
.hero{position:absolute;left:0;top:0;width:784px;height:318px;
  background:linear-gradient(160deg,#7f93a3 0%,#5f6f76 35%,#4b5a4a 60%,#2f3a36 100%)}
.hero-car{position:absolute;right:40px;top:95px;width:380px;height:170px;border-radius:60px 90px 30px 30px;
  background:radial-gradient(ellipse at 55% 45%,#4a4f55 0%,#2c3034 60%,rgba(30,34,38,0) 72%)}
.site-header{position:absolute;left:0;top:0;width:784px;height:80px}
.brand{position:absolute;left:22px;top:18px;display:flex;align-items:center;gap:8px}
.brand-dot{width:26px;height:26px;border-radius:50%;background:var(--yellow)}
.brand-name{font-weight:800;font-size:26px;color:var(--white);letter-spacing:.3px}
.contact-top{position:absolute;right:22px;top:12px;display:flex;gap:20px;font-size:9.5px;color:var(--white);font-weight:600}
.contact-top span{display:flex;align-items:center;gap:5px}
.main-nav{position:absolute;right:22px;top:40px;display:flex;gap:4px}
.main-nav a{font-size:9.5px;font-weight:700;color:var(--white);text-decoration:none;padding:6px 9px;letter-spacing:.3px}
.main-nav a.active{background:var(--yellow);color:var(--ink)}
.hero-copy{position:absolute;left:22px;top:170px}
.hero-title{font-size:34px;font-weight:700;color:var(--white);letter-spacing:.5px;line-height:1}
.hero-tag{margin-top:10px;display:flex;align-items:center;gap:6px}
.tag-yellow{background:var(--yellow);color:var(--ink);font-weight:700;font-size:20px;padding:4px 10px;font-family:"Roboto Condensed",sans-serif}
.tag-get{background:var(--dark);color:var(--white);font-size:14px;padding:5px 8px;font-weight:700}
.hero-sub{margin-top:10px;display:inline-block;background:rgba(20,28,34,.8);color:var(--white);font-size:14px;font-weight:600;padding:5px 12px;letter-spacing:.6px}
.slider-dots{position:absolute;right:24px;top:306px;display:flex;gap:5px}
.slider-dots i{width:6px;height:6px;border-radius:50%;background:rgba(255,255,255,.6)}
.slider-dots i:first-child{background:var(--white)}

/* Why */
.why{position:absolute;left:0;top:318px;width:784px;height:250px;background:var(--white)}
.why-heading{position:absolute;left:230px;top:22px;width:324px;height:32px;border:1px solid var(--line);text-align:center;
  font-weight:700;font-size:15px;line-height:30px;color:var(--ink)}
.why-heading .accent{color:var(--blue)}
.why-heading .y{color:var(--yellow)}
.why-cap{position:absolute;left:376px;top:12px;width:32px;height:18px;background:var(--white);display:flex;justify-content:center}
.why-intro{position:absolute;left:140px;top:66px;width:504px;text-align:center;font-size:9px;color:var(--muted)}

/* Audience cards */
.audience{position:absolute;left:92px;top:428px;width:600px;display:flex;gap:26px}
.aud-card{flex:1;height:144px;background:linear-gradient(180deg,var(--blue) 0%,var(--blue-deep) 100%);color:var(--white);position:relative;
  box-shadow:0 3px 8px rgba(0,0,0,.25)}
.aud-icon{position:absolute;left:50%;top:10px;transform:translateX(-50%);width:40px;height:40px;border-radius:50%;background:var(--white);display:flex;align-items:center;justify-content:center}
.aud-title{position:absolute;left:0;top:56px;width:100%;text-align:center;font-size:13px;font-weight:700}
.aud-text{position:absolute;left:18px;top:76px;right:18px;text-align:center;font-size:8.5px;line-height:1.45;opacity:.95}
.aud-more{position:absolute;left:0;bottom:10px;width:100%;text-align:center;font-size:8px;font-weight:700;letter-spacing:.6px}

/* How it works */
.how{position:absolute;left:0;top:568px;width:784px;height:307px;background:linear-gradient(180deg,#27323b 0%,#1c252c 100%)}
.how-title{position:absolute;left:0;top:30px;width:100%;text-align:center;font-size:17px;font-weight:700;color:var(--white);letter-spacing:1px}
.how-rule{position:absolute;left:372px;top:54px;width:40px;height:10px;display:flex;justify-content:center}
.steps{position:absolute;left:92px;top:82px;width:600px;display:flex;gap:18px}
.step{flex:1;background:var(--white);height:198px}
.step-img{height:122px}
.step-img.map{background:linear-gradient(135deg,#5aa9cf,#2b6f95)}
.step-img.form{background:linear-gradient(135deg,#6c9a3c,#2f5b2a)}
.step-img.buy{background:linear-gradient(135deg,#8fb6d0,#3e6b8a)}
.step-title{font-size:10.5px;font-weight:800;padding:8px 10px 3px;color:var(--ink)}
.step-text{font-size:8.5px;color:var(--muted);padding:0 10px;line-height:1.45}

/* Testimonial + form */
.trust{position:absolute;left:0;top:875px;width:784px;height:165px;background:linear-gradient(90deg,#1f3a56,#24496b)}
.trust-photo{position:absolute;left:0;top:0;width:230px;height:165px;background:linear-gradient(120deg,#c9a67d,#8a6a4d 60%,#2b3e55)}
.quote{position:absolute;left:246px;top:18px;width:190px;color:var(--white)}
.quote-name{font-size:14px;font-weight:700;letter-spacing:.4px}
.quote-role{font-size:9px;color:var(--yellow);margin-top:1px}
.quote-text{font-size:8.5px;line-height:1.5;margin-top:8px;opacity:.9}
.quote-arrows{position:absolute;left:340px;top:124px;display:flex;gap:4px}
.quote-arrows span{width:16px;height:16px;background:var(--white);display:flex;align-items:center;justify-content:center}
.cert-panel{position:absolute;left:455px;top:0;width:329px;height:165px;background:var(--blue);clip-path:polygon(28px 0,100% 0,100% 100%,0 100%)}
.cert-badge{position:absolute;left:420px;top:58px;width:54px;height:54px;border-radius:50%;background:var(--yellow);border:4px solid var(--white)}
.cert-title{position:absolute;left:510px;top:10px;font-size:13px;font-weight:700;color:var(--white);letter-spacing:.5px}
.cert-form{position:absolute;left:510px;top:30px;width:250px;display:flex;flex-direction:column;gap:5px}
.cert-form .field{height:20px;background:var(--white);font-size:8px;color:#8a9096;padding:0 7px;line-height:20px}
.cert-form .send{width:54px;height:20px;background:var(--dark);color:var(--white);font-size:8.5px;font-weight:700;text-align:center;line-height:20px;margin-top:2px}

/* Footer */
.site-footer{position:absolute;left:0;top:1040px;width:784px;height:130px;background:var(--footer);color:var(--white)}
.foot-col h4{font-size:11px;font-weight:700;letter-spacing:.6px;margin-bottom:8px}
.reach{position:absolute;left:24px;top:16px;font-size:8.5px}
.reach p{display:flex;gap:6px;margin-bottom:6px;color:#c8cfd4}
.reach b{color:var(--yellow);font-weight:700;width:14px}
.news{position:absolute;left:262px;top:16px;width:260px;text-align:center}
.news-dot{width:30px;height:30px;border-radius:50%;background:var(--yellow);margin:0 auto 6px}
.news p{font-size:8.5px;color:#c8cfd4;margin-bottom:8px}
.news-input{display:flex;height:22px}
.news-input span{flex:1;background:#101820;font-size:8px;color:#aab2b8;line-height:22px;text-align:left;padding-left:8px}
.news-input i{width:24px;background:var(--blue);display:flex;align-items:center;justify-content:center}
.connect{position:absolute;right:24px;top:16px;width:130px;text-align:right}
.connect p{font-size:8.5px;color:#c8cfd4;display:flex;align-items:center;justify-content:flex-end;gap:8px;margin-bottom:5px}
.connect p i{width:16px;height:16px;border-radius:50%;background:var(--white)}
.foot-bar{position:absolute;left:0;top:1170px;width:784px;height:30px;background:var(--footer-bar);color:#9aa3a9;font-size:8px;display:flex;justify-content:space-between;align-items:center;padding:0 24px}
</style>
</head>
<body>

<section class="hero" role="img" aria-label="Photo of a dark hatchback driving on a winding coastal road">
  <div class="hero-car"></div>
</section>

<header class="site-header">
  <div class="brand"><span class="brand-dot"></span><span class="brand-name">Tollo</span></div>
  <div class="contact-top">
    <span><svg width="9" height="9" viewBox="0 0 24 24"><path fill="#fff" d="M6.6 10.8a15 15 0 006.6 6.6l2.2-2.2a1 1 0 011-.25 11.4 11.4 0 003.6.6 1 1 0 011 1V20a1 1 0 01-1 1A17 17 0 013 4a1 1 0 011-1h3.5a1 1 0 011 1 11.4 11.4 0 00.6 3.6 1 1 0 01-.25 1z"/></svg>Toll Free: (800) 555-0142</span>
    <span><svg width="10" height="8" viewBox="0 0 24 18"><rect x="1" y="1" width="22" height="16" fill="none" stroke="#fff" stroke-width="2"/><path d="M1 1l11 9 11-9" fill="none" stroke="#fff" stroke-width="2"/></svg>hello@tollo-inspect.com</span>
  </div>
  <nav class="main-nav">
    <a class="active" href="#">WHY TOLLO</a>
    <a href="#">TOLLO CERTIFIED</a>
    <a href="#">HOW IT WORKS</a>
    <a href="#">ABOUT US</a>
    <a href="#">FAQS</a>
    <a href="#">CONTACT US</a>
  </nav>
</header>

<div class="hero-copy">
  <div class="hero-title cond">TRUSTED SELLERS...</div>
  <div class="hero-tag"><span class="tag-yellow">SMART BUYERS</span><span class="tag-get">Get</span><span class="tag-yellow">TOLLO</span></div>
  <div class="hero-sub">USED CAR INSPECTIONS</div>
</div>
<div class="slider-dots"><i></i><i></i><i></i></div>

<section class="why">
  <h2 class="why-heading"><span class="y">Why</span> Get A <span class="accent">Tollo</span> Used Car Inspection?</h2>
  <div class="why-cap"><svg width="22" height="14" viewBox="0 0 22 14"><path d="M2 10l3-6h12l3 6v3H2z" fill="#ffc214"/><circle cx="6" cy="12" r="2" fill="#2b2f33"/><circle cx="16" cy="12" r="2" fill="#2b2f33"/></svg></div>
  <p class="why-intro">Every inspection is done by trained, independent mechanics so you know exactly what you are buying before you pay.</p>
</section>

<div class="audience">
  <article class="aud-card">
    <div class="aud-icon"><svg width="22" height="20" viewBox="0 0 24 22"><path d="M1 2h4l3 12h12l3-9H6" fill="none" stroke="#33a6d7" stroke-width="2.2"/><circle cx="10" cy="19" r="2" fill="#33a6d7"/><circle cx="18" cy="19" r="2" fill="#33a6d7"/></svg></div>
    <h3 class="aud-title">FOR BUYERS</h3>
    <p class="aud-text">Book a full inspection before you buy and drive away with peace of mind and a clear report.</p>
    <div class="aud-more">READ MORE</div>
  </article>
  <article class="aud-card">
    <div class="aud-icon"><svg width="20" height="20" viewBox="0 0 24 24"><circle cx="12" cy="7" r="5" fill="#33a6d7"/><path d="M2 23c0-6 4.5-9 10-9s10 3 10 9z" fill="#33a6d7"/></svg></div>
    <h3 class="aud-title">FOR SELLERS</h3>
    <p class="aud-text">Show buyers your car is sound with a certified report that builds trust and helps you sell faster.</p>
    <div class="aud-more">READ MORE</div>
  </article>
</div>

<section class="how">
  <h2 class="how-title cond">HOW IT WORKS</h2>
  <div class="how-rule"><svg width="40" height="8" viewBox="0 0 40 8"><line x1="0" y1="4" x2="14" y2="4" stroke="#fff"/><circle cx="20" cy="4" r="3" fill="#ffc214"/><line x1="26" y1="4" x2="40" y2="4" stroke="#fff"/></svg></div>
  <div class="steps">
    <article class="step">
      <div class="step-img map" role="img" aria-label="World map with location pins"></div>
      <h3 class="step-title">FIND A LOCATION</h3>
      <p class="step-text">Search our map to find an approved inspection center close to you.</p>
    </article>
    <article class="step">
      <div class="step-img form" role="img" aria-label="Car on a forest road seen through a windscreen"></div>
      <h3 class="step-title">PERSONA/VEHICLE INFO FORM</h3>
      <p class="step-text">Tell us about yourself and the vehicle you want to have inspected.</p>
    </article>
    <article class="step">
      <div class="step-img buy" role="img" aria-label="Handshake over car keys after a purchase"></div>
      <h3 class="step-title">PURCHASE</h3>
      <p class="step-text">Pay securely online and get your full report within one day.</p>
    </article>
  </div>
</section>

<section class="trust">
  <div class="trust-photo" role="img" aria-label="Portrait of a smiling customer"></div>
  <blockquote class="quote">
    <div class="quote-name">DALE RENWICK</div>
    <div class="quote-role">Tollo customer</div>
    <p class="quote-text">Tollo checked the car before I bought it and found a brake problem the seller never mentioned. Worth every cent.</p>
  </blockquote>
  <div class="quote-arrows">
    <span><svg width="6" height="8" viewBox="0 0 6 8"><path d="M5 0L0 4l5 4z" fill="#2b2f33"/></svg></span>
    <span><svg width="6" height="8" viewBox="0 0 6 8"><path d="M1 0l5 4-5 4z" fill="#2b2f33"/></svg></span>
  </div>
  <div class="cert-panel"></div>
  <div class="cert-badge"></div>
  <h3 class="cert-title">TOLLO CERTIFIED</h3>
  <form class="cert-form">
    <div class="field">Name</div>
    <div class="field">Email</div>
    <div class="field">Phone Number</div>
    <div class="field">Car Model</div>
    <div class="send">Send</div>
  </form>
</section>

<footer class="site-footer">
  <div class="foot-col reach">
    <h4>REACH US</h4>
    <p><b>Ph.</b>(123) 555-0188</p>
    <p><b>Fx.</b>(123) 555-0199</p>
    <p><b>
      <svg width="10" height="8" viewBox="0 0 24 18"><rect x="1" y="1" width="22" height="16" fill="none" stroke="#ffc214" stroke-width="2"/><path d="M1 1l11 9 11-9" fill="none" stroke="#ffc214" stroke-width="2"/></svg>
    </b>hello@tollo-inspect.com</p>
  </div>
  <div class="news">
    <div class="news-dot"></div>
    <p>Join our newsletter for tips on buying a used car.</p>
    <div class="news-input"><span>Enter your Email Here To Subscribe</span><i><svg width="8" height="8" viewBox="0 0 8 8"><path d="M1 0l6 4-6 4z" fill="#fff"/></svg></i></div>
  </div>
  <div class="foot-col connect">
    <h4>STAY CONNECTED</h4>
    <p>Friendly <i></i></p>
    <p>Chirper <i></i></p>
    <p>Workline <i></i></p>
  </div>
</footer>
<div class="foot-bar"><span>© Tollo 2015. All Rights Reserved.</span><span>Term &amp; Conditions | Privacy</span></div>

</body>
</html>
```